Nobre Lente Lusitana - business card

Create a business card for my eyewear (glasses) store. The concept is based in handcrafted glasses (as well as common frames and 3d printed), clean, and elegant. The business card could be black (white letters and symbols) or white (black letters and symbols) but we are open to new suggestions. It must be sober and elegant.
The name Nobre Lente Lusitana means Royal/Real Portuguese Optical Store.
Our concept should be inspired by the pictures attatched bellow.
I would like it to be classic and elegant as business cards for bankers.
Our first selected logo is also available in attachment files.

Target Market(s)

For business meetings with investors, supliers and fairs

Industry/Entity Type

Eyewear

Contact Information for Business Card

Some random business cards in attachment that we like. Don't be closed to it, we like freedom of think.

Font styles to use
Serif
Sans Serif

Colors
404040
e9e9e9
fbfbfb
000000
85abd3
0255a3
f7fbfd
959595

Requirements
Must have
• Must be elegant, simple.
• Must present our brand new logo (slight variations are welcome, the logo is not closed yet). See our temporary logo in attachment.
• Black (or dark grey), white (or light grey) and a third slight color.
• This third slight color could be dark blue or grayish blue.
• Info:
• Fernando Amaral (name)
• famaral@nobrelentelusitana.example
• +351 936204518
• www.nobrelentelusitana.example
Nice to have
• Black and white or with serious colors such as dark blue or greyish blue.
• Could also have water mark with our logo (big size) in the background (inspired in KVN bank credit card design)
Should not have
• Hysteric colora or shapes

```html
<!DOCTYPE html>
<html lang="pt">
<head>
<meta charset="utf-8">
<title>Nobre Lente Lusitana – Business Card</title>
<link href="https://fonts.googleapis.com/css2?family=Roboto+Slab:wght@500&family=Teko:wght@500&family=Open+Sans:wght@400&display=swap" rel="stylesheet">
<style>
  :root {
    --backdrop: #2b2b2b;
    --brand-blue: #0255a3;
    --card-white: #e9e9e9;
    --silver: #d6d6d6;
    --ink: #404040;
  }
  * { margin: 0; padding: 0; box-sizing: border-box; }
  html, body {
    width: 1200px;
    height: 896px;
    overflow: hidden;
    background: var(--backdrop);
  }
  .canvas {
    position: relative;
    width: 1200px;
    height: 896px;
  }
  .card {
    position: absolute;
    left: 353px;
    width: 486px;
    height: 278px;
    border-radius: 18px;
  }
  .card--front {
    top: 161px;
    background: var(--brand-blue);
    display: flex;
    align-items: center;
    justify-content: center;
  }
  .brand-name {
    font-family: "Roboto Slab", serif;
    font-weight: 500;
    color: var(--silver);
    font-size: 30px;
    line-height: 1.45;
    letter-spacing: 0.32em;
    text-align: center;
    padding-left: 0.32em;
  }
  .brand-name span { display: block; }
  .card--back {
    top: 469px;
    background: var(--card-white);
  }
  .contact-line {
    position: absolute;
    left: 59px;
    top: 126px;
    display: flex;
    align-items: center;
  }
  .holder-name {
    font-family: "Teko", sans-serif;
    font-weight: 500;
    font-size: 29px;
    line-height: 1;
    color: var(--brand-blue);
    letter-spacing: 0.01em;
    padding-top: 5px;
  }
  .divider {
    width: 1.5px;
    height: 26px;
    background: var(--brand-blue);
    margin: 0 8px 0 9px;
  }
  .contact-details {
    font-family: "Open Sans", sans-serif;
    font-size: 11.5px;
    line-height: 1.25;
    color: var(--ink);
  }
</style>
</head>
<body>
  <main class="canvas">
    <section class="card card--front">
      <h1 class="brand-name">
        <span>NOBRE</span>
        <span>LENTE</span>
        <span>LUSITANA</span>
      </h1>
    </section>

    <section class="card card--back">
      <div class="contact-line">
        <p class="holder-name">FERNANDO AMARAL</p>
        <div class="divider"></div>
        <div class="contact-details">
          <p>famaral@nobrelentelusitana.example</p>
          <p>www.nobrelentelusitana.example</p>
        </div>
      </div>
    </section>
  </main>
</body>
</html>
```